Quote Cards With TK May 2025 for Instagram

I would like to put these quotes over one of the pictures attached; Instagram (new size: 4:5 (1080 x 1350 pixels) One Quote per picture, and I want the quote to be bold or easy to read as well. I provided a few reference graphics that I really like as examples below. In very small letters at the bottom add @TKBarlowOnline

All of the pictures are attached; you can pick any photo and add one quote to it; but no stock photography

```html
<!DOCTYPE html>
<html lang="en">
<head>
<meta charset="UTF-8">
<title>Quote Card – Hormones</title>
<link rel="stylesheet" href="https://fonts.googleapis.com/css2?family=Bebas+Neue&family=Oswald:wght@600&display=swap">
<style>
  :root {
    --ink-white: #ffffff;
    --accent-pink: #ff1493;
    --shade-black: #050505;
    --crowd-blue: #2f5fd6;
    --crowd-navy: #1c2a5c;
    --outfit-mauve: #a0668f;
    --ball-orange: #b5652e;
    --skin-warm: #b07d62;
    --outfit-black: #121214;
    --seat-grey: #6d6f78;
    --jacket-white: #dcdde3;
  }
  * { margin: 0; padding: 0; box-sizing: border-box; }
  html, body {
    width: 960px;
    height: 1200px;
    overflow: hidden;
    background: var(--shade-black);
  }
  .quote-card {
    position: relative;
    width: 960px;
    height: 1200px;
    overflow: hidden;
  }
  .quote-card__photo {
    position: absolute;
    inset: 0;
    background:
      /* basketball */
      radial-gradient(circle at 420px 570px, var(--ball-orange) 0, rgba(181,101,46,0.85) 70px, transparent 110px),
      /* phone-holding hand area */
      radial-gradient(ellipse 60px 90px at 600px 440px, rgba(176,125,98,0.8) 0, transparent 100%),
      /* faces as soft warm tones */
      radial-gradient(ellipse 70px 90px at 340px 330px, rgba(176,125,98,0.75) 0, transparent 100%),
      radial-gradient(ellipse 70px 90px at 690px 400px, rgba(176,125,98,0.75) 0, transparent 100%),
      radial-gradient(ellipse 60px 70px at 510px 290px, rgba(200,160,130,0.6) 0, transparent 100%),
      radial-gradient(ellipse 60px 70px at 180px 230px, rgba(190,140,120,0.55) 0, transparent 100%),
      radial-gradient(ellipse 50px 60px at 720px 230px, rgba(190,150,130,0.55) 0, transparent 100%),
      radial-gradient(ellipse 50px 60px at 880px 330px, rgba(170,120,100,0.55) 0, transparent 100%),
      radial-gradient(ellipse 50px 70px at 40px 330px, rgba(190,130,120,0.5) 0, transparent 100%),
      /* mauve outfit, left woman */
      radial-gradient(ellipse 170px 230px at 270px 610px, var(--outfit-mauve) 0, rgba(160,102,143,0.7) 55%, transparent 100%),
      /* black outfit, right woman */
      radial-gradient(ellipse 260px 320px at 740px 720px, var(--outfit-black) 0, rgba(18,18,20,0.9) 60%, transparent 100%),
      /* white jacket right edge */
      radial-gradient(ellipse 70px 220px at 930px 560px, var(--jacket-white) 0, transparent 100%),
      /* light seats lower left */
      radial-gradient(ellipse 140px 260px at 70px 960px, rgba(200,200,205,0.55) 0, transparent 100%),
      /* blue crowd shirts */
      radial-gradient(ellipse 200px 170px at 630px 160px, var(--crowd-blue) 0, transparent 100%),
      radial-gradient(ellipse 180px 140px at 900px 150px, var(--crowd-blue) 0, transparent 100%),
      radial-gradient(ellipse 160px 90px at 230px 40px, var(--crowd-blue) 0, transparent 100%),
      radial-gradient(ellipse 90px 160px at 20px 300px, rgba(47,95,214,0.7) 0, transparent 100%),
      /* grey crowd */
      radial-gradient(ellipse 220px 200px at 130px 380px, var(--seat-grey) 0, transparent 100%),
      radial-gradient(ellipse 200px 150px at 420px 160px, rgba(60,60,70,0.9) 0, transparent 100%),
      linear-gradient(180deg, #2b2f45 0%, #1f2030 55%, #141418 100%);
  }
  .quote-card__shade {
    position: absolute;
    inset: 0;
    background: linear-gradient(180deg,
      rgba(5,5,5,0) 0%,
      rgba(5,5,5,0) 55%,
      rgba(5,5,5,0.55) 64%,
      rgba(5,5,5,0.72) 80%,
      rgba(5,5,5,0.8) 100%);
  }
  .quote-card__quote {
    position: absolute;
    left: 0;
    right: 0;
    top: 716px;
    text-align: center;
    font-family: "Bebas Neue", "Oswald", sans-serif;
    font-size: 88px;
    line-height: 77px;
    letter-spacing: 1px;
    word-spacing: 6px;
    color: var(--ink-white);
    text-transform: uppercase;
  }
  .quote-card__quote .accent { color: var(--accent-pink); }
  .quote-card__handle {
    position: absolute;
    left: 0;
    right: 0;
    top: 1137px;
    text-align: center;
    font-family: "Oswald", sans-serif;
    font-weight: 600;
    font-size: 18px;
    color: var(--ink-white);
    text-transform: uppercase;
  }
</style>
</head>
<body>
  <main class="quote-card">
    <div class="quote-card__photo" role="img" aria-label="Photo of two smiling women seated courtside at a basketball game, one in a mauve top holding a basketball and the other in black taking a phone photo, with fans in blue shirts behind them"></div>
    <div class="quote-card__shade"></div>
    <p class="quote-card__quote">
      Tired. Moody. Stubborn<br>
      <span class="accent">Belly fat</span>. Your<br>
      Hormones are<br>
      Screaming for help!<br>
      <span class="accent">Let’s fix that</span>
    </p>
    <p class="quote-card__handle">@TKBarlowOnline</p>
  </main>
</body>
</html>
```